TARPLOAD business card design

TARPLOAD is a manufacturer of skip bags supplying both the domestic and commercial market. We wish to convey core characteristics of strength, professionalism and reliability to our customers. We are after a business card that uses our company colours of black and yellow as well as incorporating our logo. Our customers are predominantly in the construction or hardware industry. It is important the cards are professional as we are a small company wishing to appear larger than we actually are. more info on the company and product available at www.tarpload-example.com.au

Target Market(s)

hardware buyers, contruction company owners

Industry/Entity Type

Construction

Requirements
Must have
• company colours of black and yellow - No other colours or variation of yellow black. our company logo. card design must convey "tough"
• Card design must be landscape
• Details to be included on the card are:
• Name and Tiltle
• Phone number : 1300 41 62 53
• Mobile: 0452 718 903
• Fax: 03 9617 4852
• email: dale.hendry@tarpload-example.com.au
• address: PO Box 517, Kelvindale, VIC,3294
• Text in white when on a black background
Nice to have
• I like the idea of the back of the card being black with lighter circle area in the middle with black logo in the centre. Similar to the attached "iconic" card

```html
<!DOCTYPE html>
<html lang="en">
<head>
<meta charset="utf-8">
<title>TARPLOAD Business Card</title>
<link href="https://fonts.googleapis.com/css2?family=Carlito:wght@400;700&display=swap" rel="stylesheet">
<style>
  :root {
    --brand-yellow: #ecd000;
    --label-yellow: #d4b400;
    --ink: #000000;
    --paper: #ffffff;
    --edge: #b4b4b4;
  }
  * { margin: 0; padding: 0; box-sizing: border-box; }
  html, body {
    width: 1200px;
    height: 609px;
    overflow: hidden;
    background: var(--paper);
    font-family: "Carlito", "Calibri", sans-serif;
  }
  .canvas {
    position: relative;
    width: 1200px;
    height: 609px;
  }

  /* Card back */
  .card-back {
    position: absolute;
    left: 0;
    top: 0;
    width: 573px;
    height: 344px;
    background: var(--brand-yellow);
  }
  .brand-block {
    position: absolute;
    text-align: center;
    color: var(--ink);
    font-weight: 700;
  }
  .wordmark {
    font-size: 52px;
    line-height: 1;
    letter-spacing: 1px;
  }
  .tagline {
    font-size: 15px;
    letter-spacing: 0.5px;
    margin-top: 10px;
  }
  .card-back .brand-block {
    left: 0;
    width: 100%;
    top: 140px;
  }

  /* Card front */
  .card-front {
    position: absolute;
    left: 626px;
    top: 206px;
    width: 574px;
    height: 345px;
    background: var(--paper);
    border: 2px solid var(--edge);
    border-right: none;
  }
  .accent-band {
    position: absolute;
    left: 270px;
    top: 0;
    right: 2px;
    height: 13px;
    background: var(--brand-yellow);
  }
  .card-front .brand-block {
    left: 22px;
    top: 226px;
    width: 212px;
  }
  .card-front .wordmark { font-size: 44px; }
  .card-front .tagline { font-size: 13px; margin-top: 9px; }

  .identity {
    position: absolute;
    right: 25px;
    top: 58px;
    text-align: right;
  }
  .person-name {
    font-size: 23px;
    font-weight: 700;
    color: var(--ink);
    line-height: 1.2;
  }
  .person-title {
    font-size: 19px;
    color: var(--label-yellow);
    line-height: 1.3;
  }

  .contact-list {
    position: absolute;
    right: 24px;
    list-style: none;
    text-align: right;
    font-size: 16.5px;
    color: var(--ink);
  }
  .contact-list li { line-height: 22.5px; }
  .contact-list .label { color: var(--label-yellow); }
  .contact-phones { top: 141px; }
  .contact-online { top: 233px; }
</style>
</head>
<body>
<div class="canvas">

  <section class="card-back" aria-label="Card back">
    <div class="brand-block">
      <div class="wordmark">TARPLOAD</div>
      <div class="tagline">TOUGH ON EVERY SITE</div>
    </div>
  </section>

  <section class="card-front" aria-label="Card front">
    <div class="accent-band"></div>

    <div class="brand-block">
      <div class="wordmark">TARPLOAD</div>
      <div class="tagline">TOUGH ON EVERY SITE</div>
    </div>

    <div class="identity">
      <div class="person-name">Dale Hendry</div>
      <div class="person-title">Managing Director</div>
    </div>

    <ul class="contact-list contact-phones">
      <li><span class="label">T:</span> 1300&nbsp; 41 62 53</li>
      <li><span class="label">M:</span> 0452 718 903</li>
      <li><span class="label">F:</span> 03 9617 4852</li>
    </ul>

    <ul class="contact-list contact-online">
      <li><span class="label">W:</span> www.tarpload-example.com.au</li>
      <li><span class="label">E:</span> dale.hendry@tarpload-example.com.au</li>
      <li><span class="label">A:</span> PO Box 517, Kelvindale, VIC, 3294</li>
    </ul>
  </section>

</div>
</body>
</html>
```